Real Estate Entrepreneur needs a business card

I am a real estate entrepreneur, I buy houses for investment purposes, I act as a real estate agent representing buyers and sellers in residential home transactions, I am a contractor that does a wide range of home repairs and construction. I'd like a design that can stick with me through the years as my business grows and morphs to fit any niche I decide to pursue as markets change.

Target Market(s)

Anyone with interest that may be related to real estate.

Industry/Entity Type

Real Estate

Contact Information for Business Card

A card that stands out and doesn't put me in any one box. My business will evolve over time and I need a card that can stay relevant.

Colors

Designer to choose colors to be used in the design.

Requirements
Must have
• Character
Nice to have
• I'm open
Should not have
• Cliche houses and hammers

```html
<!DOCTYPE html>
<html lang="en">
<head>
<meta charset="utf-8">
<title>Reid Calloway — Business Card</title>
<link rel="stylesheet" href="https://fonts.googleapis.com/css2?family=Jost:wght@400&display=swap">
<style>
  :root {
    --backdrop: #141414;
    --card: #333333;
    --ink: #f4f4f4;
    --ink-soft: #d9d9d9;
    --band-strong: rgba(255,255,255,0.16);
    --band-clear: rgba(255,255,255,0);
  }
  * { margin: 0; padding: 0; box-sizing: border-box; }
  html, body {
    width: 1200px; height: 900px; overflow: hidden;
    background: var(--backdrop);
    font-family: "Jost", "Futura", sans-serif;
  }
  .stage {
    width: 1200px; height: 900px;
    display: flex; flex-direction: column; align-items: center; justify-content: center;
    gap: 40px;
  }
  .card {
    position: relative;
    width: 560px; height: 320px;
    background: var(--card);
    overflow: hidden;
    box-shadow: 0 14px 30px rgba(0,0,0,0.55);
  }
  .dot-band {
    position: absolute;
    left: -10%; width: 120%;
    height: 70px;
    background: linear-gradient(to bottom, var(--band-clear), var(--band-strong) 50%, var(--band-clear));
  }
  .card--back .dot-band { top: 10px; }
  .card--front .dot-band { top: 6px; }
  .card__name {
    position: absolute;
    color: var(--ink);
    font-weight: 400;
    letter-spacing: 0.5px;
  }
  .card--back .card__name { left: 44px; bottom: 48px; font-size: 30px; }
  .card--front .card__name {
    left: 0; right: 0; top: 148px;
    text-align: center; font-size: 40px;
  }
  .contact {
    position: absolute;
    right: 40px; top: 112px;
    list-style: none;
    color: var(--ink-soft);
    font-size: 15px;
    line-height: 22px;
  }
  .contact__item { display: flex; align-items: center; gap: 12px; }
  .contact__icon { width: 13px; height: 13px; flex: none; }
</style>
</head>
<body>
<main class="stage">
  <section class="card card--back">
    <div class="dot-band" role="img" aria-label="Diagonal band of fine white halftone dots"></div>
    <ul class="contact">
      <li class="contact__item">
        <svg class="contact__icon" viewBox="0 0 14 14"><path d="M1 5c0-2 2-3 6-3s6 1 6 3l-3 1-1-2H5L4 6zM3 7h8l1 5H2z" fill="#d9d9d9"/></svg>
        (555) 214 - 0376
      </li>
      <li class="contact__item">
        <svg class="contact__icon" viewBox="0 0 14 14"><rect x="3.5" y="1" width="7" height="12" rx="1" fill="none" stroke="#d9d9d9" stroke-width="1.4"/></svg>
        (555) 608 - 4721
      </li>
      <li class="contact__item">
        <svg class="contact__icon" viewBox="0 0 14 14"><rect x="1" y="3" width="12" height="8" fill="#d9d9d9"/><path d="M1 3l6 5 6-5" fill="none" stroke="#333" stroke-width="1"/></svg>
        info@reidcalloway.com
      </li>
      <li class="contact__item">
        <svg class="contact__icon" viewBox="0 0 14 14"><g fill="none" stroke="#d9d9d9" stroke-width="1.2"><circle cx="7" cy="7" r="5.8"/><ellipse cx="7" cy="7" rx="2.5" ry="5.8"/><path d="M1.2 7h11.6"/></g></svg>
        www.reidcalloway.com
      </li>
    </ul>
    <h1 class="card__name">Reid Calloway</h1>
  </section>

  <section class="card card--front">
    <div class="dot-band" role="img" aria-label="Diagonal band of fine white halftone dots"></div>
    <h2 class="card__name">Reid Calloway</h2>
  </section>
</main>
</body>
</html>
```